A Pocket Guide to QLV - The Onboarding Magazine

We need a magazine/booklet design for an internal marketing booklet. All of the content is currently in a PDF format, and we have attached all the QLV branding elements. We need the booklet tidied up and made into an editable PDF booklet so that we can make changes as required. The primary brand colours are red and black however we want this project to feel fun, adventurous and inspirational. It would be great if you could work off the work that has been done so far but it needs a professional to look at it and touch it up. This booklet is for new onboarding employee to understand and navigate their new company gaining company context and to have a fun creative booklet to refer too for any information that they might need.
We are waiting on some more information on page 5 and intend to add two more staff members on there with profile pictures and information description.
Page 12 only requires the text on the page however we are struggling for inspiration as to how to display this. page 25-26 are blank as I would like the PDF 'QLV employee benefits' that I am attaching to be included this information does not need editing however if you feel it needs to be changed a little to be in keeping with this magazine style then please do.

Target Market(s)

new employees joining QLV

Industry/Entity Type

Insurance

Font styles to use
Sans Serif
Other font styles liked:
• Garet

Colors
EB3D1F
EC4F4E
F09395
F8D3D4
FCEDEE

Requirements
Must have
• A fluid look to it, visually we are looking for a sleek modern and fun feel. All written information must be kept in.
Nice to have
• all images are taken off the internet if there are images you can visualize that relate to the used ones that might look better then please use
Should not have
• A corporate feel to it. This booklet must remain fun, adventurous and inspirational

```html
<!DOCTYPE html>
<html lang="en">
<head>
<meta charset="utf-8">
<title>A Pocket Guide to QLV – Booklet Spreads</title>
<link rel="stylesheet" href="https://fonts.googleapis.com/css2?family=Open+Sans:wdth,wght@75..100,300..800&display=swap">
<style>
:root{
  --backdrop:#727377;
  --red:#EB3D1F;
  --red-soft:#EC4F4E;
  --brand-red:#E8323A;
  --blush:#F8D3D4;
  --blush-light:#FCEDEE;
  --ink:#3a3a3c;
  --ink-dark:#222224;
  --white:#ffffff;
  --sky:#a9c9ee;
}
*{margin:0;padding:0;box-sizing:border-box}
html,body{width:900px;height:1200px;overflow:hidden}
body{background:var(--backdrop);font-family:"Open Sans",Arial,sans-serif;color:var(--ink);position:relative}
.page{position:absolute;width:315px;height:445px;background:var(--white);overflow:hidden}
.page--cover{left:109px;top:129px}
.page--contents{left:476px;top:129px}
.page--big-picture{left:109px;top:625px;background:var(--blush)}
.page--welcome{left:476px;top:625px}

.brand-mark{position:absolute;left:22px;top:23px;height:33px;width:128px;background:var(--white);display:flex;align-items:center;gap:8px}
.brand-mark__square{width:33px;height:33px;background:var(--brand-red);flex:none}
.brand-mark__name{font-weight:800;font-size:11px;letter-spacing:1.6px;color:var(--ink-dark);text-transform:uppercase}

.partner-row{position:absolute;left:0;right:0;top:392px;height:35px;display:flex;align-items:center;justify-content:space-between;padding:0 22px 0 24px}
.partner{display:flex;align-items:center;gap:4px;font-weight:700;font-size:8.5px;color:var(--ink-dark);line-height:1.05}
.partner__square{width:9px;height:9px;background:var(--ink-dark);flex:none}
.footer-bar{position:absolute;left:0;right:0;bottom:0;height:9px;background:var(--brand-red)}

/* Cover */
.cover__hero{position:absolute;left:0;top:72px;width:315px;height:298px;background:linear-gradient(180deg,rgba(255,255,255,0) 0%,var(--sky) 8%,#c6dbf3 55%,var(--white) 100%)}
.cover__title{position:absolute;left:64px;top:92px;font-weight:300;font-size:38px;line-height:53px;color:var(--ink);letter-spacing:-0.5px}
.cover__title-accent{position:absolute;left:64px;top:199px;font-weight:800;font-size:42px;line-height:1;color:var(--brand-red);letter-spacing:-0.5px}
.cover__ribbon{position:absolute;left:67px;right:0;top:244px;height:21px;background:var(--brand-red);color:var(--white);font-weight:700;font-stretch:75%;font-size:8.5px;line-height:21px;padding-left:6px}

/* Contents */
.contents__band{position:absolute;left:0;top:0;width:315px;height:54px;background:var(--blush)}
.contents__heading{position:absolute;left:67px;top:96px;font-weight:300;font-size:29px;color:var(--brand-red);letter-spacing:0.3px}
.contents__list{position:absolute;left:68px;top:142px;width:197px;list-style:none}
.contents__item{display:flex;align-items:baseline;height:16px;font-size:7.4px;color:var(--ink)}
.contents__label{white-space:nowrap}
.contents__dots{flex:1;border-bottom:1px dotted var(--ink);margin:0 2px 0 2px;transform:translateY(-2px);max-width:calc(100% - 0px)}
.contents__page{width:26px;text-align:right;color:var(--brand-red)}

/* Big picture */
.big-picture__curve{position:absolute;left:0;top:0}
.big-picture__kicker{position:absolute;left:67px;top:89px;font-weight:300;font-size:28px;color:var(--ink)}
.big-picture__kicker b{font-weight:800;color:var(--brand-red)}
.big-picture__title{position:absolute;left:65px;top:111px;font-weight:300;font-size:46px;line-height:1;color:var(--ink)}
.big-picture__welcome{position:absolute;left:68px;top:174px;font-weight:700;font-size:8.4px;color:var(--ink-dark)}
.big-picture__body{position:absolute;left:68px;top:198px;width:226px;font-size:8.2px;line-height:15.9px;color:var(--ink)}

/* Welcome */
.welcome__line1{position:absolute;left:49px;top:41px;font-weight:300;font-size:20px;color:var(--ink);line-height:1}
.welcome__band{position:absolute;left:0;top:86px;width:315px;height:32px;background:var(--brand-red)}
.welcome__line2{position:absolute;left:48px;top:60px;font-weight:300;font-size:26px;color:var(--ink);line-height:1}
.welcome__accent{position:absolute;left:141px;top:55px;font-weight:800;font-size:38px;color:var(--brand-red);line-height:1}
.welcome__crew{position:absolute;left:141px;top:89px;font-weight:300;font-size:29px;color:var(--white);line-height:1}
.welcome__lead{position:absolute;left:49px;top:128px;width:190px;font-weight:700;font-size:7.6px;line-height:10.8px;color:var(--brand-red)}
.welcome__body{position:absolute;left:49px;top:154px;width:216px;font-size:7.2px;line-height:10.6px;color:var(--ink)}
.welcome__body p{margin-bottom:5.4px}
.welcome__body p.narrow{width:138px}
.welcome__photo{position:absolute;left:95px;top:272px;width:220px;height:173px;background:radial-gradient(ellipse at 75% 70%,#8fa6c0 0%,#c9d5e2 45%,rgba(255,255,255,0) 78%)}
</style>
</head>
<body>

<section class="page page--cover">
  <div class="cover__hero" role="img" aria-label="Smiling businesswoman holding a tablet against a city sky"></div>
  <div class="brand-mark"><span class="brand-mark__square"></span><span class="brand-mark__name">QLV Agencies</span></div>
  <h1 class="cover__title">A POCKET<br>GUIDE TO</h1>
  <div class="cover__title-accent">QLV</div>
  <div class="cover__ribbon">Quill Lane Ventures</div>
  <div class="partner-row">
    <span class="partner"><span class="partner__square"></span>Trailhead<br>Cover</span>
    <span class="partner"><span class="partner__square"></span>Fernleaf Insurance</span>
    <span class="partner"><span class="partner__square"></span>Toolbox<br>Trade Cover</span>
  </div>
  <div class="footer-bar"></div>
</section>

<section class="page page--contents">
  <div class="contents__band"></div>
  <div class="brand-mark"><span class="brand-mark__square"></span><span class="brand-mark__name">QLV Agencies</span></div>
  <h2 class="contents__heading">CONTENT</h2>
  <ul class="contents__list">
    <li class="contents__item"><span class="contents__label">Big Picture</span><span class="contents__dots"></span><span class="contents__page">4</span></li>
    <li class="contents__item"><span class="contents__label">Welcome to the QLV crew</span><span class="contents__dots"></span><span class="contents__page">5</span></li>
    <li class="contents__item"><span class="contents__label">Meet the crew</span><span class="contents__dots"></span><span class="contents__page">6</span></li>
    <li class="contents__item"><span class="contents__label">A brief history of QLV</span><span class="contents__dots"></span><span class="contents__page">7</span></li>
    <li class="contents__item"><span class="contents__label">Quill Lane Ventures - B2C brand</span><span class="contents__dots"></span><span class="contents__page">8</span></li>
    <li class="contents__item"><span class="contents__label">Information on Trailhead Cover</span><span class="contents__dots"></span><span class="contents__page">10</span></li>
    <li class="contents__item"><span class="contents__label">Information on Fernleaf Insurance</span><span class="contents__dots"></span><span class="contents__page">11</span></li>
    <li class="contents__item"><span class="contents__label">Information on Toolbox</span><span class="contents__dots"></span><span class="contents__page">12</span></li>
    <li class="contents__item"><span class="contents__label">The Values of QLV (the 4 B’s)</span><span class="contents__dots"></span><span class="contents__page">13-18</span></li>
    <li class="contents__item"><span class="contents__label">The QLV strategy</span><span class="contents__dots"></span><span class="contents__page">19-23</span></li>
    <li class="contents__item"><span class="contents__label">Staff support</span><span class="contents__dots"></span><span class="contents__page">24</span></li>
    <li class="contents__item"><span class="contents__label">Glossary of insurance terms</span><span class="contents__dots"></span><span class="contents__page">25-27</span></li>
  </ul>
  <div class="partner-row">
    <span class="partner"><span class="partner__square"></span>Trailhead<br>Cover</span>
    <span class="partner"><span class="partner__square"></span>Fernleaf Insurance</span>
    <span class="partner"><span class="partner__square"></span>Toolbox<br>Trade Cover</span>
  </div>
  <div class="footer-bar"></div>
</section>

<section class="page page--big-picture">
  <svg class="big-picture__curve" width="315" height="445" viewBox="0 0 315 445" aria-hidden="true">
    <path d="M0 330 Q157 440 315 330 L315 445 L0 445 Z" fill="#ffffff"/>
  </svg>
  <div class="brand-mark"><span class="brand-mark__square"></span><span class="brand-mark__name">QLV Agencies</span></div>
  <h2 class="big-picture__kicker">THE <b>BIG</b></h2>
  <div class="big-picture__title">PICTURE</div>
  <p class="big-picture__welcome">Welcome!</p>
  <p class="big-picture__body">You've landed a great role within one of the best and most innovative industries. The insurance market in Australia is a well-regulated, professional and competitive industry to be in. At the end of 2021 the gross value of Insurance in Australia was $156 Billion. A robust and competitive insurance industry is a common attribute in all modern and developed countries. This industry enables individuals, businesses and the government to have confidence when investing in infrastructure.</p>
  <div class="partner-row">
    <span class="partner"><span class="partner__square"></span>Trailhead<br>Cover</span>
    <span class="partner"><span class="partner__square"></span>Fernleaf Insurance</span>
    <span class="partner"><span class="partner__square"></span>Toolbox<br>Trade Cover</span>
  </div>
  <div class="footer-bar"></div>
</section>

<section class="page page--welcome">
  <div class="welcome__band"></div>
  <div class="welcome__line1">WELCOME</div>
  <div class="welcome__line2">TO THE</div>
  <div class="welcome__accent">QLV</div>
  <div class="welcome__crew">CREW</div>
  <p class="welcome__lead">You are now onboard at QLV, which makes you part of the crew!</p>
  <div class="welcome__body">
    <p>If you're wondering what's in store for you as you embark on your journey then this book will tell you.  It is filled with lots of information about what we do, why we do it and how you can be a part of it.</p>
    <p>This is just the beginning. We don't expect you to know everything all at once. Like the rest of us you'll be learning all the time. That's one of the things that makes QLV so great - the sky is the limit.</p>
    <p>We hired you because we think you've got what it takes to have a positive impact on the future of QLV.</p>
    <p class="narrow">Now is the time to improve your skills, develop your career and hopefully have a great time along the way.</p>
  </div>
  <div class="welcome__photo" role="img" aria-label="Group of smiling young colleagues stacking hands together, seen from below"></div>
</section>

</body>
</html>
```